Chamber of Commerce Web Design Project

We are working with Marigold Chamber of Commerce. They are a new chamber of commerce forming in SoCal.
Some sites to use for inspiration:
https://brevenlochamber.org
https://varnidel.org
https://www.quoratlinchamber.com
https://www.wtchamber.com
https://morvendipcc.org
Thank you for taking the time to consider designing a website for us. We are web developers based in Stockton, CA, USA. Most of our projects go through the same process. Understanding this process may help you win a project with us. We custom-code all of our websites in-house. We don’t have any requirements as to what tools you use for your design, but we prefer Figma files. For any design that we label as four-stars, we send it to the client for review. The client picks the final design they want us to use. Once we complete this process, we will continue to show additional clients all the four-star sites and purchase them later. Your designs will have multiple chances to sell. For better chances of success, we ask that you follow these guidelines.
IMAGES:
If you use any images or icons in the design, we ask that you have a link to the asset so we can purchase the image/icon. Most of the designs we submit do not have the customer’s images on them unless they have some great images. Be creative; show us the feeling you are trying to portray with your image choices. Use any royalty-free site you choose. We subscribe to Adobe and mainly use their images, but we can purchase images outside of Adobe.
PLEASE NOTE: we will not submit designs to clients with watermarks on the images.
FONTS:
We ask that you identify the fonts used in the design. This can be done in a message if you want. We typically use Google Fonts and Adobe Fonts.
CONTENT:
We're always open to different content and ideas. We often submit designs with stock images so the client can see our vision. We typically take pictures after the website launch to use their images with our vision. Lorem Ipsum is fine for paragraphs, but we ask that you write the headers in correct English. We want to be able to show the vision and identify the sections of the website.
INSPIRATION:
We typically add a couple of links in the brief of websites we like to help you get started in your design.
REVISIONS:
We do not often ask for revisions of the designs unless we see something in the design that may not appeal to the client. If there are slight changes that we want to make, we do that in the development process.
FEEDBACK:
We rarely give feedback on designs during the design process. We are working on many website projects and do not have the time to provide feedback. We usually respond if your request is well thought out and asks specific questions, but a note asking “feedback, please” usually goes unanswered.

```html
<!DOCTYPE html>
<html lang="en">
<head>
<meta charset="utf-8">
<title>Marigold Chamber of Commerce</title>
<link href="https://fonts.googleapis.com/css2?family=Bebas+Neue&family=Poppins:ital,wght@0,400;0,500;0,600;1,400&display=swap" rel="stylesheet">
<style>
:root{
  --blue:#1778f2;
  --blue-dark:#0f62d0;
  --ink:#2b2b2b;
  --text:#3a3a3a;
  --muted:#6b6b6b;
  --line:#e4e4e4;
  --gold:#f6c21a;
  --white:#fff;
}
*{box-sizing:border-box;margin:0;padding:0}
html,body{width:1200px;height:4508px;overflow:hidden}
body{position:relative;background:var(--white);font-family:"Poppins",sans-serif;color:var(--text)}
.abs{position:absolute}
.display{font-family:"Bebas Neue",sans-serif;color:var(--ink);font-weight:400;letter-spacing:-.5px;line-height:1}
.eyebrow{color:var(--blue);font-size:19px;font-weight:500;display:flex;align-items:center;gap:10px;white-space:nowrap}
.eyebrow i{display:block;width:44px;height:2px;background:var(--blue)}
.copy{font-size:13px;line-height:24px;color:var(--text);text-align:justify}
.btn{position:absolute;display:flex;align-items:center;justify-content:center;gap:10px;background:var(--blue);color:#fff;border-radius:20px;font-size:15px;font-weight:500}
.btn .dot{width:15px;height:15px;border-radius:50%;background:var(--gold);display:flex;align-items:center;justify-content:center}
.photo{position:absolute}

/* header */
.brand{left:66px;top:40px;display:flex;align-items:center;gap:10px;color:var(--blue);font-size:22px;font-weight:600;white-space:nowrap}
.brand b{width:34px;height:34px;border-radius:50%;background:var(--blue);display:block}
.nav a{position:absolute;top:70px;font-size:13px;color:var(--ink);text-decoration:none}
.nav a.active{color:var(--blue)}
.nav a.active::after{content:"";position:absolute;left:0;right:0;bottom:-7px;height:2px;background:var(--gold)}
.nav .pill{top:63px;left:1027px;width:107px;height:32px;background:var(--blue);color:#fff;border-radius:16px;display:flex;align-items:center;justify-content:center;font-size:13px}

/* hero */
.hero{left:0;top:150px;width:1200px;height:699px;background:linear-gradient(180deg,#6e7268 0%,#5d6a57 50%,#4d5f46 100%)}
.hero-text{left:0;width:1200px;text-align:center;color:#fff}
.dots span{position:absolute;top:806px;width:11px;height:11px;border-radius:50%;background:#fff}
.dots span.on{width:17px;height:17px;top:803px;background:transparent;border:3px solid var(--blue);box-shadow:inset 0 0 0 2px #fff}

/* services */
.card{position:absolute;top:2021px;height:301px;background:#fff;border-radius:0 30px 0 0;box-shadow:0 0 0 1px var(--line),3px 3px 8px rgba(0,0,0,.06);padding:0 22px}
.card.featured{background:var(--blue);border-radius:30px 0 0 0;box-shadow:none}
.card svg{position:absolute;top:36px;left:22px}
.card h3{position:absolute;top:96px;left:22px;right:22px;font-size:14.5px;font-weight:500;line-height:19px;color:var(--blue);text-transform:uppercase}
.card p{position:absolute;top:164px;left:22px;right:22px;font-size:12.5px;line-height:24px;text-align:justify;color:var(--text)}
.card.featured h3,.card.featured p{color:#fff}
.card.featured h3{top:86px}

/* blog */
.post-img{position:absolute;top:3281px;width:310px;height:196px}
.post-body{position:absolute;top:3378px;width:190px;height:140px;background:#fff;padding:16px 0 0 12px}
.post-body .date{font-size:11px;color:var(--muted)}
.post-body h4{font-size:19px;font-weight:400;color:var(--blue);margin-top:6px;line-height:22px}
.post-body p{font-size:11.5px;line-height:19px;color:var(--text)}
.post-body em{display:block;margin-top:10px;font-size:11px;color:var(--blue)}
.arrow{position:absolute;top:3385px;width:40px;height:40px;border-radius:50%;background:#fff;box-shadow:0 1px 5px rgba(0,0,0,.18);display:flex;align-items:center;justify-content:center}

/* contact */
.field{position:absolute;background:#fff;border:1px solid var(--line);box-shadow:0 2px 5px rgba(0,0,0,.08);font-size:13px;color:#555;padding:0 20px;display:flex;align-items:center}

/* footer */
.footer{left:0;top:4207px;width:1200px;height:301px;background:var(--blue);color:#fff}
.footer h5{position:absolute;top:74px;font-size:15px;font-weight:500;padding-left:12px;border-left:2px solid #fff;line-height:22px}
.footer .links li{list-style:none;font-size:13.5px;height:28px;display:flex;align-items:center;gap:6px}
.footer .links li::before{content:"";width:10px;height:10px;border-radius:50%;background:rgba(255,255,255,.7)}
.ci{position:absolute;left:624px;display:flex;gap:14px;font-size:12px;line-height:14px}
.ci b{width:24px;height:24px;border:1px solid #fff;border-radius:3px;display:flex;align-items:center;justify-content:center;flex:none}
.social{position:absolute;top:4400px;display:flex;gap:6px;left:72px}
.social span{width:26px;height:26px;border:1.5px solid #fff;border-radius:3px}
</style>
</head>
<body>

<!-- header -->
<div class="abs brand"><b></b>Marigold</div>
<nav class="nav">
  <a class="active" style="left:404px">HOME</a>
  <a style="left:502px">ABOUT US</a>
  <a style="left:623px">SERVICES</a>
  <a style="left:742px">MEMBER RESOURCES</a>
  <a style="left:934px">EVENTS</a>
  <a class="pill">CONTACT US</a>
</nav>

<!-- hero -->
<section class="abs hero" role="img" aria-label="Industrial pipeline facility with valves and grey pipework"></section>
<div class="abs hero-text" style="top:330px;font-size:24px">WELCOME TO</div>
<h1 class="abs hero-text display" style="top:388px;font-size:80px;color:#fff;letter-spacing:0">MARIGOLD CHAMBER OF COMMERCE</h1>
<p class="abs hero-text" style="top:496px;font-size:21px;line-height:32px;padding:0 230px">Lorem ipsum dolor sit amet, consectetur adipiscing elit, sed do eiusmod tempor incididunt ut labore et dolore magna aliqua.</p>
<a class="btn" style="left:513px;top:595px;width:173px;height:39px;font-size:17px">CONTACT US <span class="dot"><svg width="7" height="8"><path d="M1 0l5 4-5 4z" fill="var(--blue)"/></svg></span></a>
<div class="dots"><span class="on" style="left:548px"></span><span style="left:586px"></span><span style="left:611px"></span><span style="left:637px"></span></div>

<!-- about -->
<div class="abs" style="left:154px;top:1031px;width:359px;height:395px;border:2px solid var(--blue);border-radius:12px"></div>
<div class="photo" style="left:77px;top:959px;width:310px;height:389px;background:linear-gradient(135deg,#cfd4d8,#8e969c);border-radius:6px" role="img" aria-label="Stainless steel pipework in a plant room"></div>
<div class="photo" style="left:287px;top:1124px;width:310px;height:388px;background:linear-gradient(135deg,#d9b98f 0%,#b6c3cf 55%,#3c4556 100%);border-radius:6px;border:6px solid #fff" role="img" aria-label="Team of business professionals standing together"></div>
<h2 class="abs display" style="left:686px;top:1060px;font-size:56px">ABOUT US</h2>
<div class="abs eyebrow" style="left:686px;top:1120px">WHO WE ARE <i></i></div>
<p class="abs copy" style="left:693px;top:1176px;width:394px">Lorem ipsum dolor sit amet, consectetur adipiscing elit, sed do eiusmod tempor incididunt ut labore et dolore magna aliqua. Quis ipsum suspendisse ultrices gravida. Risus commodo viverra maecenas accumsan lacus vel facilisis. Lorem ipsum dolor sit amet, consectetur adipiscing elit, sed do eiusmod tempor incididunt ut labore et dolore magna aliqua.</p>
<a class="btn" style="left:693px;top:1379px;width:156px;height:35px">KNOW MORE <span class="dot"><svg width="7" height="8"><path d="M1 0l5 4-5 4z" fill="var(--blue)"/></svg></span></a>

<!-- services -->
<h2 class="abs display" style="left:0;width:1200px;text-align:center;top:1776px;font-size:56px">OUR SERVICES</h2>
<div class="abs eyebrow" style="left:0;width:1200px;justify-content:center;top:1838px"><i></i>WHAT WE DO<i></i></div>
<p class="abs" style="left:256px;width:689px;top:1899px;text-align:center;font-size:13px;line-height:24px">Lorem ipsum dolor sit amet, consectetur adipiscing elit, sed do eiusmod tempor incididunt ut labore et dolore magna aliqua. Quis ipsum suspendisse ultrices gravida. Risus commodo viverra maecenas</p>

<div class="card featured" style="left:98px;width:252px">
  <svg width="46" height="46" viewBox="0 0 46 46" fill="none" stroke="#fff" stroke-width="2"><circle cx="23" cy="23" r="8"/><circle cx="7" cy="7" r="4"/><circle cx="39" cy="7" r="4"/><circle cx="7" cy="39" r="4"/><circle cx="39" cy="39" r="4"/><path d="M10 10l7 7M36 10l-7 7M10 36l7-7M36 36l-7-7"/></svg>
  <h3>Business<br>Connections</h3>
  <p>Lorem ipsum dolor sit amet, consectetur adipiscing elit, sed do eiusmod tempor incididunt ut labore et dolore magna aliqua. Quis ipsum</p>
</div>
<div class="card" style="left:350px;width:242px">
  <svg width="48" height="48" viewBox="0 0 48 48" fill="none" stroke="var(--blue)" stroke-width="2"><circle cx="20" cy="20" r="13"/><path d="M29 29l12 12"/><path d="M13 24l5-6 4 4 5-7"/></svg>
  <h3>Market Research</h3>
  <p>Lorem ipsum dolor sit amet, consectetur adipiscing elit, sed do eiusmod tempor incididunt ut labore et dolore magna aliqua. Quis ipsum</p>
</div>
<div class="card" style="left:595px;width:249px">
  <svg width="46" height="46" viewBox="0 0 46 46" fill="none" stroke="var(--blue)" stroke-width="2"><rect x="6" y="10" width="34" height="26" rx="2"/><path d="M14 30v-6M21 30v-10M28 30v-8M34 30v-13"/><path d="M18 40h10"/></svg>
  <h3>Marketing<br>Consultation</h3>
  <p>Lorem ipsum dolor sit amet, consectetur adipiscing elit, sed do eiusmod tempor incididunt ut labore et dolore magna aliqua. Quis ipsum</p>
</div>
<div class="card" style="left:847px;width:250px">
  <svg width="50" height="46" viewBox="0 0 50 46" fill="none" stroke="var(--blue)" stroke-width="2"><circle cx="25" cy="12" r="7"/><path d="M14 30c0-6 5-10 11-10s11 4 11 10"/><path d="M4 20v16l10 6M46 20v16l-10 6"/></svg>
  <h3>Talent &amp;<br>Workforce</h3>
  <p>Lorem ipsum dolor sit amet, consectetur adipiscing elit, sed do eiusmod tempor incididunt ut labore et dolore magna aliqua. Quis ipsum</p>
</div>

<!-- member resources -->
<h2 class="abs display" style="left:68px;top:2614px;font-size:58px">MEMBER RESOURCES</h2>
<div class="abs eyebrow" style="left:66px;top:2678px">MARIGOLD CHAMBER OF COMMERCE <i></i></div>
<p class="abs copy" style="left:69px;top:2748px;width:394px">Lorem ipsum dolor sit amet, consectetur adipiscing elit, sed do eiusmod tempor incididunt ut labore et dolore magna aliqua. Quis ipsum suspendisse ultrices gravida. Risus commodo viverra maecenas accumsan lacus vel facilisis. Lorem ipsum dolor sit amet, consectetur adipiscing elit, sed do eiusmod tempor incididunt ut labore et dolore magna aliqua.</p>
<a class="btn" style="left:72px;top:2964px;width:129px;height:35px">EXPLORE <span class="dot"><svg width="7" height="8"><path d="M1 0l5 4-5 4z" fill="var(--blue)"/></svg></span></a>
<div class="abs" style="left:812px;top:2560px;width:364px;height:459px;border:2px solid var(--blue)"></div>
<div class="photo" style="left:578px;top:2597px;width:556px;height:383px;background:linear-gradient(160deg,#dfe3e6 0%,#a9b2b8 55%,#5f676d 100%)" role="img" aria-label="Business people walking along a covered walkway"></div>

<!-- blog -->
<h2 class="abs display" style="left:0;width:1200px;text-align:center;top:3156px;font-size:56px">LATEST BLOG</h2>
<div class="abs eyebrow" style="left:0;width:1200px;justify-content:center;top:3213px"><i style="width:28px"></i>NEWS &amp; UPDATES<i style="width:28px"></i></div>

<div class="arrow" style="left:24px"><svg width="8" height="12"><path d="M7 1L2 6l5 5" stroke="#333" fill="none" stroke-width="1.5"/></svg></div>
<div class="arrow" style="left:1147px"><svg width="8" height="12"><path d="M1 1l5 5-5 5" stroke="#333" fill="none" stroke-width="1.5"/></svg></div>

<div class="post-img" style="left:84px;background:linear-gradient(135deg,#c9ced3,#7a8590)" role="img" aria-label="Colleagues talking in an office kitchen"></div>
<div class="post-body" style="left:204px"><div class="date">Friday JAN 24, 2025</div><h4>Post 1 Headline</h4><p>Lorem ipsum dolor sit amet,<br>consectetur adipi</p><em>Read More</em></div>

<div class="post-img" style="left:445px;background:linear-gradient(135deg,#5d6a74,#c8ccd0)" role="img" aria-label="Business meeting around a table"></div>
<div class="post-body" style="left:565px"><div class="date">Saturday JAN 25, 2025</div><h4>Post 2 Headline</h4><p>Lorem ipsum dolor sit amet,<br>consectetur adipi</p><em>Read More</em></div>

<div class="post-img" style="left:803px;background:linear-gradient(135deg,#c3cdd8,#6b7684)" role="img" aria-label="Team working together at a bright office desk"></div>
<div class="post-body" style="left:923px"><div class="date">Friday JAN 25, 2023</div><h4>Post 3 Headline</h4><p>Lorem ipsum dolor sit amet,<br>consectetur adipi</p><em>Read More</em></div>

<!-- contact -->
<div class="abs" style="left:21px;top:3630px;width:298px;height:477px;border:2px solid var(--blue)"></div>
<div class="photo" style="left:68px;top:3670px;width:454px;height:381px;background:linear-gradient(160deg,#dfe8f2 0%,#b8c6d6 45%,#3e5fa5 100%)" role="img" aria-label="Large industrial pipes on a blue steel frame under the sky"></div>
<h2 class="abs display" style="left:578px;top:3656px;font-size:56px">CONTACT US</h2>
<i class="abs" style="left:832px;top:3685px;width:46px;height:2px;background:var(--blue)"></i>
<p class="abs" style="left:585px;top:3735px;width:555px;font-size:13px;line-height:24px">Lorem ipsum dolor sit amet, consectetur adipiscing elit, sed do eiusmod tempor incid idunt ut labore et dolore magna aliqua. Quis ipsum suspendisse ultrices</p>
<div class="field" style="left:583px;top:3812px;width:268px;height:50px">Your Name</div>
<div class="field" style="left:870px;top:3812px;width:268px;height:50px">Phone Number</div>
<div class="field" style="left:583px;top:3875px;width:555px;height:52px">Email Address</div>
<div class="field" style="left:583px;top:3941px;width:555px;height:96px;align-items:flex-start;padding-top:16px">Message</div>
<a class="btn" style="left:581px;top:4076px;width:114px;height:35px">SUBMIT <span class="dot"><svg width="7" height="8"><path d="M1 0l5 4-5 4z" fill="var(--blue)"/></svg></span></a>

<!-- footer -->
<footer class="abs footer">
  <div class="abs" style="left:70px;top:56px;display:flex;align-items:center;gap:10px;font-size:26px;font-weight:600"><b style="width:36px;height:36px;border-radius:50%;background:#fff;display:block"></b>Marigold</div>
  <p class="abs" style="left:70px;top:128px;font-size:12.5px;line-height:19px">Lorem ipsum dolor sit amet,<br>consectetur adipiscing elit</p>

  <h5 style="left:370px">QUICK LINKS</h5>
  <ul class="abs links" style="left:386px;top:109px"><li>About Us</li><li>Services</li><li>Membership</li><li>Contact Us</li></ul>

  <h5 style="left:611px">CONTACT US</h5>
  <div class="ci" style="top:112px"><b><svg width="12" height="12" viewBox="0 0 12 12"><path d="M2 1l2 0 1 3-1.5 1a6 6 0 0 0 3 3L8 6.5l3 1v2L10 11C5 11 1 7 1 2z" fill="#fff"/></svg></b><div>CALL US<br>xxxx xxx xxx</div></div>
  <div class="ci" style="top:156px"><b><svg width="12" height="10"><rect x=".5" y=".5" width="11" height="9" fill="none" stroke="#fff"/><path d="M.5 .5l5.5 5 5.5-5" fill="none" stroke="#fff"/></svg></b><div>EMAIL US<br>info@marigoldchamber.org</div></div>
  <div class="ci" style="top:200px"><b><svg width="10" height="13" viewBox="0 0 10 13"><path d="M5 12S1 7 1 5a4 4 0 0 1 8 0c0 2-4 7-4 7z" fill="none" stroke="#fff" stroke-width="1.3"/><circle cx="5" cy="5" r="1.4" fill="#fff"/></svg></b><div>Address line Dummy Here<br>Address line Here</div></div>

  <h5 style="left:926px">NEWSLETTER SIGN UP</h5>
  <p class="abs" style="left:941px;top:112px;font-size:12.5px;line-height:17px">Subscribe our newsletter to<br>get the latest news.</p>
  <div class="abs" style="left:941px;top:172px;width:197px;height:29px;background:#fff;border-radius:2px;color:#888;font-size:11.5px;display:flex;align-items:center;padding-left:8px">Enter Email Address
    <span style="position:absolute;right:6px;top:5px;width:26px;height:19px;border-radius:10px;background:var(--blue);display:flex;align-items:center;justify-content:center"><svg width="14" height="8"><path d="M0 4h12M9 1l3 3-3 3" stroke="#fff" fill="none" stroke-width="1.4"/></svg></span></div>

  <div class="abs" style="left:70px;top:247px;width:1068px;height:1px;background:rgba(255,255,255,.7)"></div>
  <p class="abs" style="left:0;width:1200px;top:262px;text-align:center;font-size:11.5px">Copyright © 2025 All Rights Reserved By Company name</p>
</footer>
<div class="social"><span></span><span></span><span></span><span></span></div>

</body>
</html>
```